Tranquil Pathway Business Card

Logo attached. (will be printing onto thick white/off white textured card)

Double sided business card for two Therapists working at Tranquil Pathway.

Require one design, but with different name and mobile numbers on each card.

Target Market(s)

Medical, Health

Industry/Entity Type

Business

Contact Information for Business Card

Need one business card design, but a separate card for each person - Colin Marchetti and Marieke de Boeckx.

FRONT OF CARD

Logo

Name (Colin Marchetti on one card, Marieke de Boeckx on the other)
Professional Clinical Hypnotherapist

Consulting Rooms (Near Lindqvist Hospital)
482 Brackenfield Road
Dunmore VIC 3987

Colin@TranquilPathway.example.au OR Marieke@TranquilPathway.example.au

Mobile: 0455 872 604 (for Colin) OR
Mobile: 0467 290 518 (for Marieke)

BACK OF CARD

Logo

Website: www.TranquilPathway.example.au

Phone: 1300 958 471

Requirements
Must have
• Text and logo only. No additiional graphics.

```html
<!DOCTYPE html>
<html lang="en">
<head>
<meta charset="utf-8">
<title>Tranquil Pathway Business Card</title>
<link rel="stylesheet" href="https://fonts.googleapis.com/css2?family=Titillium+Web:wght@300;400;600;700&display=swap">
<style>
  :root {
    --navy: #2b3590;
    --navy-deep: #1f2773;
    --navy-light: #3d4aa6;
    --silver: #a9acb3;
    --silver-light: #d9dbe0;
    --paper: #ffffff;
    --stage: #ecebe8;
    --ink-soft: #c9cdea;
  }
  * { box-sizing: border-box; margin: 0; padding: 0; }
  html, body { width: 1200px; height: 1023px; overflow: hidden; }
  body {
    background: var(--stage);
    font-family: "Titillium Web", Arial, sans-serif;
    position: relative;
  }
  .card {
    position: absolute;
    width: 700px;
    height: 428px;
    left: 250px;
    border-radius: 4px;
    overflow: hidden;
    box-shadow: 0 8px 24px rgba(0,0,0,0.18);
  }
  .card-front { top: 48px; background: var(--paper); }
  .card-back {
    top: 536px;
    background: linear-gradient(135deg, var(--navy-light) 0%, var(--navy) 45%, var(--navy-deep) 100%);
  }
  .card-art { position: absolute; inset: 0; }

  .brand-mark {
    position: absolute;
    border-radius: 50%;
    background: var(--navy);
  }
  .brand-name {
    position: absolute;
    font-weight: 700;
    text-transform: uppercase;
    line-height: 0.95;
  }

  .card-front .brand-mark { left: 44px; top: 214px; width: 136px; height: 136px; }
  .card-front .brand-name {
    left: 48px; top: 48px;
    color: var(--navy);
    font-size: 46px;
    letter-spacing: 1px;
  }

  .contact-block {
    position: absolute;
    right: 40px;
    top: 44px;
    text-align: right;
    color: var(--paper);
  }
  .person-name {
    font-size: 27px;
    font-weight: 700;
    text-transform: uppercase;
    letter-spacing: 0.5px;
    line-height: 1.1;
  }
  .person-role { font-size: 15px; font-weight: 400; color: var(--ink-soft); }
  .contact-lines { margin-top: 26px; list-style: none; }
  .contact-lines li {
    display: flex; justify-content: flex-end; align-items: center; gap: 10px;
    font-size: 15px; color: var(--ink-soft); line-height: 1.9;
  }
  .contact-icon {
    width: 20px; height: 20px; border-radius: 4px;
    background: rgba(255,255,255,0.18);
    display: inline-flex; align-items: center; justify-content: center;
  }
  .address-line {
    position: absolute;
    right: 40px; bottom: 26px;
    color: var(--ink-soft);
    font-size: 14px;
  }
  .address-line strong { font-weight: 600; color: var(--paper); }

  .card-back .brand-mark {
    left: 250px; top: 114px; width: 90px; height: 90px;
    background: var(--paper);
  }
  .card-back .brand-name {
    left: 360px; top: 126px;
    color: var(--paper);
    font-size: 36px;
    letter-spacing: 1px;
  }
  .brand-divider {
    position: absolute; left: 250px; top: 232px; width: 260px; height: 1px;
    background: var(--silver);
  }
  .back-contact {
    position: absolute;
    left: 0; right: 0; bottom: 38px;
    text-align: center;
    color: var(--ink-soft);
    font-size: 17px;
    letter-spacing: 2px;
    line-height: 1.6;
  }
</style>
</head>
<body>

<section class="card card-front" aria-label="Business card front">
  <svg class="card-art" viewBox="0 0 700 428" width="700" height="428" aria-hidden="true">
    <defs>
      <linearGradient id="band" x1="0" y1="0" x2="1" y2="1">
        <stop offset="0" stop-color="#3d4aa6"/>
        <stop offset="0.5" stop-color="#2b3590"/>
        <stop offset="1" stop-color="#1f2773"/>
      </linearGradient>
    </defs>
    <path d="M340,0 C360,170 240,340 70,428" fill="none" stroke="#a9acb3" stroke-width="12"/>
    <path d="M360,0 C380,170 260,340 90,428 L700,428 L700,0 Z" fill="url(#band)"/>
    <path d="M360,0 C380,170 260,340 90,428" fill="none" stroke="#d9dbe0" stroke-width="3"/>
  </svg>

  <div class="brand-name">Tranquil<br>Pathway</div>
  <div class="brand-mark"></div>

  <div class="contact-block">
    <h1 class="person-name">Colin Marchetti</h1>
    <p class="person-role">Professional Clinical Hypnotherapist</p>
    <ul class="contact-lines">
      <li>0455 872 604
        <span class="contact-icon">
          <svg width="12" height="12" viewBox="0 0 24 24" aria-hidden="true"><path fill="#fff" d="M6.6 10.8a15 15 0 0 0 6.6 6.6l2.2-2.2a1 1 0 0 1 1-.25 11.4 11.4 0 0 0 3.6.57 1 1 0 0 1 1 1V20a1 1 0 0 1-1 1A17 17 0 0 1 3 4a1 1 0 0 1 1-1h3.5a1 1 0 0 1 1 1c0 1.25.2 2.45.57 3.57a1 1 0 0 1-.25 1z"/></svg>
        </span>
      </li>
      <li>Colin@TranquilPathway.example.au
        <span class="contact-icon">
          <svg width="12" height="12" viewBox="0 0 24 24" aria-hidden="true"><path fill="#fff" d="M3 5h18v14H3z M3 5l9 7 9-7" stroke="#2b3590" stroke-width="1.5"/></svg>
        </span>
      </li>
      <li>482 Brackenfield Road, Dunmore VIC 3987
        <span class="contact-icon">
          <svg width="12" height="12" viewBox="0 0 24 24" aria-hidden="true"><path fill="#fff" d="M12 2a7 7 0 0 0-7 7c0 5 7 13 7 13s7-8 7-13a7 7 0 0 0-7-7zm0 9.5A2.5 2.5 0 1 1 12 6.5a2.5 2.5 0 0 1 0 5z"/></svg>
        </span>
      </li>
    </ul>
  </div>

  <p class="address-line"><strong>Consulting Rooms</strong> (Near Lindqvist Hospital)</p>
</section>

<section class="card card-back" aria-label="Business card back">
  <div class="brand-mark"></div>
  <div class="brand-name">Tranquil<br>Pathway</div>
  <div class="brand-divider"></div>
  <div class="back-contact">
    <p class="website">www.TranquilPathway.example.au</p>
    <p class="phone">1300 958 471</p>
  </div>
</section>

</body>
</html>
```